Website Online Research Solutions

We are a small European high-tech online research company.
With our own state of the art software we run online panels and are conducting reseach for companies. Partly research via our own panel and partly via panels we maintain for our customers.
Our current website is old and outdatet: www.pravelo.nl.
We are in the process to change the content of the site. We want a modern, european and businesslike design for our new website.
Our logo has to stay the same (left uppersite of our website and attached) but can be changed a little to adapt it to the new design of the website. The colors of the site are up to you.
Target Market(s)
Marketeers and researchers of large and middle size companies in all kind of fields.
Industry/Entity Type
Online
Look and feel
Each slider illustrates characteristics of the customer's brand and the style your logo design should communicate.

```html
<!DOCTYPE html>
<html lang="nl">
<head>
<meta charset="utf-8">
<title>Pravelo – Producten</title>
<link href="https://fonts.googleapis.com/css2?family=Open+Sans:wght@400;600&family=Arimo:ital,wght@0,400;0,700;1,400;1,700&display=swap" rel="stylesheet">
<style>
:root{
  --page:#ffffff;
  --bar-top:#f4f4f4;
  --bar-bottom:#e4e4e4;
  --bar-line:#d2d2d2;
  --ink:#3a3a3a;
  --ink-soft:#555a5e;
  --accent:#5b8797;
  --link:#4d7a8e;
  --banner-a:#5b646c;
  --banner-b:#2f373e;
  --foot:#3d454d;
  --foot-link:#a9b2ba;
  --rule:#c8c8c8;
  --icon-blue:#9cbcd3;
}
*{box-sizing:border-box;margin:0;padding:0}
html,body{width:1200px;height:1033px;overflow:hidden;background:var(--page)}
body{position:relative;font-family:"Arimo",Arial,sans-serif;color:var(--ink)}
.abs{position:absolute}

.topbar{left:256px;top:0;width:685px;height:37px;border:1px solid var(--bar-line);border-top:0;border-radius:0 0 4px 4px;background:linear-gradient(var(--bar-top),var(--bar-bottom))}
.login{left:22px;top:12px;font-size:9px;color:#666}
.login b{color:#444}
.search{left:478px;top:8px;width:162px;height:19px;border:1px solid #cfcfcf;border-radius:3px;background:#fff;font-size:8px;color:#999;padding:4px 6px}
.search-icon{left:644px;top:9px}

.brand{left:278px;top:44px;width:110px;height:100px}
.brand-name{left:294px;top:78px;font-family:"Open Sans",sans-serif;font-weight:600;font-size:21px;color:#4a4a4a}
.tagline{left:639px;top:79px;font-size:10.5px;font-style:italic;color:#555;line-height:13px}
.tagline b{color:#333}

.nav{left:256px;top:144px;width:685px;height:32px;border:1px solid var(--bar-line);border-radius:4px;background:linear-gradient(#fdfdfd,#e9e9e9)}
.nav ul{list-style:none;position:absolute;left:0;top:0;width:100%;height:100%}
.nav li{position:absolute;top:11px;font-size:8.5px;color:#222}
.nav li.active{top:5px;height:26px;padding:6px 7px 0;background:linear-gradient(#d9d9d9,#f6f6f6);border-radius:3px 3px 0 0;font-weight:700}

.banner{left:257px;top:200px;width:684px;height:61px;border-radius:3px;background:linear-gradient(90deg,var(--banner-a),var(--banner-b) 60%,#3b434a)}
.banner h1{position:absolute;left:29px;top:16px;font-family:"Open Sans",sans-serif;font-weight:400;font-size:24px;color:#fff;letter-spacing:-.3px}

.product h2{position:absolute;left:395px;font-family:"Open Sans",sans-serif;font-weight:400;font-size:13px;color:#333}
.product p{position:absolute;left:395px;width:340px;font-size:7.6px;line-height:13.5px;color:var(--ink-soft)}
.more{position:absolute;left:666px;font-size:8px;font-weight:700;color:var(--link);text-decoration:underline}
.more i{display:inline-block;width:10px;height:10px;border-radius:50%;background:#8a949c;margin-left:4px;vertical-align:-2px;position:relative}
.more i::after{content:"";position:absolute;left:3px;top:2px;border-left:4px solid #fff;border-top:3px solid transparent;border-bottom:3px solid transparent}
.icon{position:absolute;left:306px}
.placeholder{position:absolute;border-radius:6px}

.subnav-title{left:774px;top:275px;font-family:"Open Sans",sans-serif;font-size:17px;color:var(--accent)}
.subnav{left:769px;top:312px;width:160px;list-style:none}
.subnav li{height:23px;border-bottom:1px solid var(--rule);font-size:8px;color:#222;padding:4px 0 0 22px;position:relative}
.subnav li:last-child{border-bottom:0}
.subnav li.current{color:var(--link);text-decoration:underline}
.subnav svg{position:absolute;left:0;top:3px}

.footer{left:0;top:841px;width:1200px;height:192px;background:linear-gradient(160deg,#4a525a,var(--foot) 50%,#353d44)}
.foot-links{left:263px;top:29px;font-size:7px;color:var(--foot-link)}
.foot-links span{position:absolute;text-decoration:underline;white-space:nowrap}
.foot-links em{position:absolute;font-style:normal;color:#8b949c}
.copy{left:762px;top:29px;font-size:7px;color:#fff}
</style>
</head>
<body>

<header>
  <div class="abs topbar">
    <div class="abs login">Klant <b>Login</b></div>
    <div class="abs search">Zoek:</div>
    <svg class="abs search-icon" width="20" height="20" viewBox="0 0 20 20" aria-label="Zoeken">
      <circle cx="8" cy="8" r="6" fill="#dfeaf2" stroke="#7b9bb0" stroke-width="2"/>
      <line x1="12.5" y1="12.5" x2="18" y2="18" stroke="#5e6c76" stroke-width="3" stroke-linecap="round"/>
    </svg>
  </div>

  <svg class="abs brand" viewBox="0 0 110 100" aria-hidden="true">
    <circle cx="55" cy="46" r="46" fill="none" stroke="#4a4a4a" stroke-width="2"/>
  </svg>
  <div class="abs brand-name">Pravelo</div>

  <div class="abs tagline">Gespecialiseerd in <b>online gegevensverzameling</b><br>en analyse en is werkzaam voor internationale opdrachtgevers</div>

  <nav class="abs nav">
    <ul>
      <li style="left:345px">Algemeen</li>
      <li class="active" style="left:394px">Producten</li>
      <li style="left:456px">Demo`s</li>
      <li style="left:500px">Media</li>
      <li style="left:534px">Referenties</li>
      <li style="left:590px">Personeel</li>
      <li style="left:639px">Contact</li>
    </ul>
  </nav>
</header>

<main>
  <div class="abs banner"><h1>Producten</h1></div>

  <section class="product">
    <svg class="icon" style="top:288px" width="46" height="48" viewBox="0 0 46 48" aria-hidden="true">
      <path d="M4 14 L18 3 V9 H38 V19 H18 V25 Z" fill="#7d9db4"/>
      <path d="M42 33 L28 22 V28 H8 V38 H28 V44 Z" fill="var(--icon-blue)"/>
    </svg>
    <h2 style="top:290px">Dataverzameling</h2>
    <p style="top:320px">Vragenlijsten die door Pravelo worden geprogrammeerd zijn dynamisch gegenereerde vragenlijsten die in de "look &amp; feel" worden geprogrammeerd van onze klanten en/of de produkten van onze klanten.</p>
    <a class="more" style="top:366px">zie meer<i></i></a>

    <svg class="icon" style="top:399px;left:310px" width="44" height="44" viewBox="0 0 44 44" aria-hidden="true">
      <circle cx="17" cy="17" r="12" fill="#dce9f2" stroke="#8fa9bb" stroke-width="3"/>
      <line x1="26" y1="26" x2="38" y2="38" stroke="#5f6b74" stroke-width="5" stroke-linecap="round"/>
    </svg>
    <h2 style="top:390px">Analyse</h2>
    <p style="top:420px">Q-Tabula is een online analyse tool voor het verwerken van onderzoeksgegevens en daarbij is het 's werelds eerste dataprocessing tool die in staat is meer dan een miljoen respondenten per seconde te ver- werken.</p>
    <a class="more" style="top:468px">zie meer<i></i></a>

    <div class="placeholder" role="img" aria-label="Icoon van een klant" style="left:316px;top:491px;width:40px;height:40px;background:linear-gradient(#c7ccd1,#2c3136)"></div>
    <h2 style="top:490px">Klanten</h2>
    <p style="top:520px">Pravelo is uitgegroeid tot een volwaardig speler in de markt met een indrukwekkend(e) portfolio.</p>
    <a class="more" style="top:567px">zie meer<i></i></a>

    <svg class="icon" style="top:588px;left:318px" width="44" height="28" viewBox="0 0 44 28" aria-hidden="true">
      <path d="M2 9 H24 V2 L42 14 L24 26 V19 H2 Z" fill="var(--icon-blue)"/>
    </svg>
    <h2 style="top:592px">Dataset Publising</h2>
    <p style="top:622px">Middels onze analysetool Q-Tabula zijn wij in staat uw dataset online beschikbaar te maken voor uw klanten.</p>
    <a class="more" style="top:670px">zie meer<i></i></a>

    <div class="placeholder" role="img" aria-label="Icoon van een beeldscherm" style="left:313px;top:692px;width:44px;height:44px;background:linear-gradient(#b9d3e4,#8a9aa6)"></div>
    <h2 style="top:696px">Panel: inPolls</h2>
    <p style="top:726px">"Na onze test is gebleken: Het panel van Pravelo is een van de beste en een van de meest representatieve panels in Nederland" - Maarten Hoek (Nordveld Insights)</p>
    <a class="more" style="top:769px">zie meer<i></i></a>
  </section>

  <aside>
    <div class="abs subnav-title">Sub Navigatie</div>
    <ul class="abs subnav">
      <li class="current"><svg width="16" height="16" viewBox="0 0 16 16" aria-hidden="true"><circle cx="8" cy="8" r="8" fill="#8d979f"/><path d="M4 8 L7 11 L12 5" fill="none" stroke="#fff" stroke-width="2"/></svg>Dataverzameling</li>
      <li><svg width="16" height="16" viewBox="0 0 16 16" aria-hidden="true"><circle cx="8" cy="8" r="8" fill="#8d979f"/><path d="M4 8 L7 11 L12 5" fill="none" stroke="#fff" stroke-width="2"/></svg>Analyse</li>
      <li><svg width="16" height="16" viewBox="0 0 16 16" aria-hidden="true"><circle cx="8" cy="8" r="8" fill="#8d979f"/><path d="M4 8 L7 11 L12 5" fill="none" stroke="#fff" stroke-width="2"/></svg>Klanten</li>
      <li><svg width="16" height="16" viewBox="0 0 16 16" aria-hidden="true"><circle cx="8" cy="8" r="8" fill="#8d979f"/><path d="M4 8 L7 11 L12 5" fill="none" stroke="#fff" stroke-width="2"/></svg>Dataset Publising</li>
      <li><svg width="16" height="16" viewBox="0 0 16 16" aria-hidden="true"><circle cx="8" cy="8" r="8" fill="#8d979f"/><path d="M4 8 L7 11 L12 5" fill="none" stroke="#fff" stroke-width="2"/></svg>Panel: inPolls</li>
    </ul>
  </aside>
</main>

<footer class="abs footer">
  <div class="abs foot-links">
    <span style="left:0;top:0">Algemeen</span><em style="left:39px;top:0">|</em>
    <span style="left:49px;top:0">Producten</span>
    <span style="left:49px;top:13px">Dataverzameling</span>
    <span style="left:49px;top:26px">Analyse</span>
    <span style="left:49px;top:40px">Klanten</span>
    <span style="left:49px;top:53px">Dataset Publising</span>
    <span style="left:49px;top:67px">Panel: inPolls</span>
    <em style="left:112px;top:0">|</em><span style="left:122px;top:0">Demo`s</span>
    <em style="left:155px;top:0">|</em><span style="left:163px;top:0">Media</span>
    <em style="left:189px;top:0">|</em><span style="left:196px;top:0">Referenties</span>
    <em style="left:242px;top:0">|</em><span style="left:248px;top:0">Personeel</span>
    <em style="left:286px;top:0">|</em><span style="left:293px;top:0">Contact</span>
    <em style="left:326px;top:0">|</em><span style="left:332px;top:0">Site Map</span>
  </div>
  <div class="abs copy">© Copyright 2010. Pravelo. All Rights Reserved</div>
</footer>

</body>
</html>
```